The Brightwater Compass Business Card

We need an attractive business card with the logo that we bought from ArtVantly last year.
Our mission is to contribute to change the way today's leaders manage business companies bringing value to the workplace and helping them to build a new model of creating wealth.
Our logo is clear about our values : we seek Positive Change through People and are convinced that the pursuit of individual well-being and the chase of economic results can converge with the right management.
Management Consulting
Corinne Fabrelle
+34 612 98 70 31
corinne.fabrelle@thebrightwatercompass-mail.net
www.thebrightwatercompass-mail.net

```html
<!DOCTYPE html>
<html lang="en">
<head>
<meta charset="utf-8">
<title>The Brightwater Compass – Business Card</title>
<link rel="stylesheet" href="https://fonts.googleapis.com/css2?family=Noto+Sans:wght@400;700&display=swap">
<style>
  :root {
    --teal: #148583;
    --teal-soft: #5aa9a6;
    --mint: #cfe9e6;
    --ink: #111111;
    --grey: #555555;
    --paper: #ffffff;
    --backdrop: #ebe8e3;
  }
  html, body {
    margin: 0;
    padding: 0;
    width: 1200px;
    height: 1000px;
    overflow: hidden;
    background: var(--backdrop);
    font-family: "Noto Sans", Arial, sans-serif;
  }
  .canvas { position: relative; width: 1200px; height: 1000px; }
  .card {
    position: absolute;
    background: var(--paper);
    border-radius: 16px;
    overflow: hidden;
    box-shadow: 0 4px 10px rgba(0,0,0,0.18);
  }
  .card-front { left: 349px; top: 212px; width: 517px; height: 291px; }
  .card-back  { left: 351px; top: 536px; width: 516px; height: 294px; }

  .tree-art {
    position: absolute;
    left: 0; top: 0;
    width: 230px; height: 210px;
    background: radial-gradient(ellipse at 30% 40%, var(--teal) 0%, var(--teal-soft) 55%, rgba(90,169,166,0) 80%);
  }
  .wave { position: absolute; left: 0; bottom: 0; width: 517px; height: 100px; display: block; }

  .contact { position: absolute; left: 249px; top: 60px; }
  .contact-name { margin: 0; font-size: 19px; font-weight: 700; color: var(--ink); line-height: 24px; }
  .contact-name .surname { color: var(--teal); }
  .contact-phone { margin: 0 0 12px; font-size: 14px; color: var(--ink); line-height: 20px; }
  .contact-web { margin: 0; font-size: 14px; color: var(--grey); line-height: 18px; }

  .brand {
    position: absolute;
    left: 0; right: 0; top: 0; bottom: 0;
    display: flex; align-items: center; justify-content: center;
  }
  .brand-name {
    margin: 0;
    font-size: 30px;
    font-weight: 700;
    color: var(--teal);
    letter-spacing: 0.5px;
  }
</style>
</head>
<body>
<main class="canvas">
  <section class="card card-front">
    <div class="tree-art" role="img" aria-label="Teal tree illustration with leaves and branches"></div>
    <svg class="wave" viewBox="0 0 517 100" preserveAspectRatio="none" aria-hidden="true">
      <path d="M0 18 C120 -4 260 20 380 40 C440 50 490 40 517 18 L517 100 L0 100 Z" fill="var(--mint)"/>
      <path d="M0 28 C120 12 260 36 380 52 C440 60 490 50 517 32 L517 100 L0 100 Z" fill="var(--paper)"/>
      <path d="M0 31 C120 16 260 40 380 57 C440 64 490 54 517 38 L517 100 L0 100 Z" fill="var(--teal)"/>
    </svg>
    <div class="contact">
      <p class="contact-name">Corinne <span class="surname">Fabrelle</span></p>
      <p class="contact-phone">+34 612 98 70 31</p>
      <p class="contact-web">corinne.fabrelle<br>@thebrightwatercompass-mail.net<br>www.thebrightwatercompass-mail.net</p>
    </div>
  </section>

  <section class="card card-back">
    <div class="brand">
      <p class="brand-name">The Brightwater Compass</p>
    </div>
  </section>
</main>
</body>
</html>
```